Brochure design for joint venture

We need a 4 page A4 brochure for a joing venture between two engineering companies.A draft version of the text can be found in the attachments, along with the logo. The text pdf shows the general style and layout of hte text, but am very open to artistic advice.Image placeholders should be added on pages indicated - these are not yet availableColour scheme is orange and green, looking for strong, bold, lines. Look and feel should be clean and professional, not too cluttered.Final desing shoul dbe avialable in RGB psd format, with full layers so we can modify text and images easily.
Like the look of this style:
https://www.plarnivo.com/vector-art/483921-orange-and-green-business-brochure-design-template

```html
<!DOCTYPE html>
<html lang="en">
<head>
<meta charset="utf-8">
<title>VoltaForm &amp; CoreFlow Thermal – Brochure</title>
<link href="https://fonts.googleapis.com/css2?family=Oswald:wght@500;600&family=Open+Sans:ital,wght@0,400;0,600;0,700;0,800;1,700;1,800&display=swap" rel="stylesheet">
<style>
  :root{
    --orange:#f07a0e;
    --green:#7ab72f;
    --ink:#2a2a2a;
    --grey-bg:#6d6d6d;
    --photo-lab:#5d7a92;
    --photo-copper:#7a3a22;
    --photo-gears:#1c3d6e;
    --photo-plant:#3f4a55;
    --white:#ffffff;
  }
  *{box-sizing:border-box;margin:0;padding:0}
  html,body{width:1200px;height:1200px;overflow:hidden}
  body{background:var(--grey-bg);font-family:"Open Sans",Arial,sans-serif;color:var(--ink);position:relative}
  .page{position:absolute;width:351px;height:492px;background:var(--white);overflow:hidden;box-shadow:0 4px 14px rgba(0,0,0,.35)}
  .page--cover{left:227px;top:86px}
  .page--offerings{left:622px;top:86px}
  .page--experience{left:227px;top:622px}
  .page--contact{left:622px;top:622px}
  .abs{position:absolute}
  .photo{position:absolute}
  .brand{display:flex;align-items:center;gap:6px;font-family:"Open Sans",Arial,sans-serif;font-weight:600;font-size:16px;color:var(--white);letter-spacing:.3px;white-space:nowrap}
  .brand .dot{width:11px;height:11px;border-radius:50%;background:currentColor;display:inline-block;flex:none}
  .footer-links{position:absolute;left:0;width:100%;display:flex;justify-content:space-around;font-size:7.5px;font-weight:600;white-space:nowrap}
  .footer-links span::before{content:"";display:inline-block;width:6px;height:6px;border-radius:50%;border:1.2px solid currentColor;margin-right:3px;vertical-align:-1px}
  .green-bar{position:absolute;left:0;width:100%;background:var(--green)}
  .ticks{list-style:none}
  .ticks li{position:relative;padding-left:11px;font-size:6.4px;line-height:1.3;font-weight:600;margin-bottom:4px}
  .ticks li::before{content:"";position:absolute;left:0;top:1px;width:6px;height:6px;border-radius:50%;background:var(--orange)}
  .ticks li::after{content:"";position:absolute;left:1.8px;top:2.4px;width:1.6px;height:2.6px;border:solid var(--white);border-width:0 1px 1px 0;transform:rotate(45deg)}
  .ticks .sub{list-style:none;margin-top:3px}
  .ticks .sub li{padding-left:9px;margin-bottom:3px}
  .ticks .sub li::before{width:4px;height:4px;top:2px}
  .ticks .sub li::after{display:none}
  h2.section{font-weight:800;color:var(--orange);font-size:14px}
  h3.sub-head{font-weight:800;font-style:italic;color:var(--orange);font-size:9.5px}
  h3.block-head{font-weight:700;color:var(--orange);font-size:9.5px}
  .cover-title{left:13px;top:350px;font-family:Oswald,sans-serif;font-weight:600;font-size:26px;color:var(--orange);line-height:1;letter-spacing:-.3px;white-space:nowrap}
  .cover-subtitle{left:13px;top:381px;font-weight:800;font-size:16.5px;line-height:1;color:var(--green);letter-spacing:.2px;white-space:nowrap}
</style>
</head>
<body>

<section class="page page--cover">
  <svg class="abs" width="351" height="340" style="left:0;top:0">
    <rect x="0" y="0" width="351" height="100" fill="var(--orange)"/>
    <polygon points="316,100 351,100 351,246 300,246" fill="var(--orange)"/>
    <polygon points="316,100 330,100 292,336 282,336" fill="var(--green)"/>
  </svg>
  <div class="photo" role="img" aria-label="Engineers working together on electronic prototype in a lab"
       style="left:0;top:100px;width:316px;height:236px;clip-path:polygon(0 0,100% 0,89% 100%,0 100%);background:linear-gradient(135deg,#8aa3b6,var(--photo-lab) 55%,#3e4f60)"></div>
  <div class="brand abs" style="left:16px;top:40px"><span class="dot"></span>VoltaForm</div>
  <div class="brand abs" style="left:186px;top:40px;font-size:15px"><span class="dot"></span>CoreFlow Thermal</div>
  <h1 class="abs cover-title">A PARTNERSHIP OF ELECTRICAL</h1>
  <p class="abs cover-subtitle">MACHINE DESIGN SPECIALISTS</p>
  <div class="abs" style="left:14px;top:409px;width:325px;font-size:7.4px;line-height:1.4">
    <p style="margin-bottom:8px">Two complementary specialist companies working together to provide state-of-the art complete designs for electrical machines</p>
    <p>Located in Germany and UK, we are two complimentary electrical machines design companies, combining to provide electrical machine design services.</p>
  </div>
  <div class="footer-links" style="top:467px;color:var(--ink)"><span>www.voltaform.com</span><span>www.coreflow-thermal.co.uk</span></div>
  <div class="green-bar" style="top:483px;height:9px"></div>
</section>

<section class="page page--offerings">
  <div class="abs" style="left:0;top:0;width:351px;height:85px;background:var(--orange)"></div>
  <div class="abs" style="left:339px;top:85px;width:12px;height:117px;background:var(--orange)"></div>
  <h2 class="abs" style="left:14px;top:12px;font-weight:800;font-size:14.5px;color:var(--white)">OUR OFFERINGS</h2>
  <div class="abs" style="left:14px;top:33px;width:325px;font-size:7px;line-height:1.4;font-weight:600;color:var(--white)">
    <p style="margin-bottom:4px">We offer full electrical machine design, from the concept stage to a full set of technical drawings and manufacturing documents</p>
    <p>We also offer modifications and improvements to existing electrical machine product ranges</p>
  </div>
  <div class="photo" role="img" aria-label="Close-up of copper stator windings"
       style="left:0;top:85px;width:339px;height:181px;background:radial-gradient(ellipse at 50% 30%,#c9835a,var(--photo-copper) 55%,#2b1710)"></div>
  <h3 class="abs block-head" style="left:14px;top:273px">We are experienced in:</h3>
  <ul class="ticks abs" style="left:14px;top:290px;width:150px">
    <li>Synchronous machines</li>
    <li>Permanent Magnet machines</li>
  </ul>
  <ul class="ticks abs" style="left:176px;top:290px;width:160px">
    <li>Induction machines, including Doubly Fed Induction Generators (DFIG)</li>
  </ul>
  <h3 class="abs block-head" style="left:14px;top:321px">Specific design expertise include:</h3>
  <ul class="ticks abs" style="left:14px;top:340px;width:160px">
    <li>High Efficiency designs : up to 98.2% (10MW)</li>
    <li>Thermal management solutions for increased power density, reduced costs and increased product lifetime</li>
    <li>Design optimisation for technical specifications: cost, weight and manufacturability</li>
    <li>Modular approach</li>
  </ul>
  <ul class="ticks abs" style="left:176px;top:340px;width:160px">
    <li>Robust vibration proven designs: up to 30 year lifetime</li>
    <li>Validation plans &amp; test data evaluation for mechanical, electrical and thermal performance</li>
    <li>Root cause analysis – failure investigation</li>
  </ul>
  <p class="abs" style="left:13px;top:427px;width:325px;font-size:8.6px;line-height:1.5;font-weight:700;color:var(--orange)">Our highly skilled engineers work closely with customers to deliver designs according to set specification</p>
  <div class="green-bar" style="top:470px;height:16px"></div>
  <div class="footer-links" style="top:474px;color:var(--white)"><span>www.voltaform.com</span><span>www.coreflow-thermal.co.uk</span></div>
</section>

<section class="page page--experience">
  <h2 class="abs section" style="left:14px;top:12px">OUR EXPERIENCE</h2>
  <h3 class="abs sub-head" style="left:14px;top:34px">WHY WORK WITH US?</h3>
  <ul class="ticks abs" style="left:14px;top:50px;width:325px">
    <li>A complete package: Electromagnetic Design, Mechanical Design, Thermal Design &amp; Manufacturing engineering</li>
    <li>Extensive application experience: Marine, stationary power plant, industrial, oil/gas offshore, hydro, wind</li>
    <li>Machine designs with world best efficiency (98.2% at 10MW)</li>
    <li>Robust designs withstanding high vibration levels – e.g. driven by gas / diesel engines for up to 30 year lifetime</li>
    <li>Modular approach, integrated product design and serial product knowledge: parts reduced by up to 75%</li>
    <li>Comprehensive validation program using in depth Multiphysics FEA simulations to prove detailed test data</li>
    <li>Advanced modelling software, customised for electrical machine analysis</li>
  </ul>
  <h3 class="abs sub-head" style="left:14px;top:187px">Our experiences</h3>
  <ul class="ticks abs" style="left:14px;top:203px;width:325px">
    <li>Pool of specialists with more than 150 years of combined experience in Electrical Machine Design: Electromagnetic, Mechanical, Thermal &amp; Manufacturing</li>
    <li>Extensive experience cutting across industry and academia</li>
    <li>Experience working with companies including Nordwerk, Halvard, Electrovia, Brennan Power and University of Eastmoor Electrical Machines Department</li>
    <li>R&amp;D experiences of conventional and novel electrical machines, including simulation and implementation of novel thermal solutions</li>
    <li>5 commercial products developed - from concept via prototype to serial production
      <ul class="sub">
        <li>Up to 20MW; 400V – 15kV</li>
        <li>500rpm – 1800rpm</li>
        <li>Up to 80 tons</li>
      </ul>
    </li>
    <li>International customer base</li>
  </ul>
  <div class="photo" role="img" aria-label="Two engineers reviewing plans in an industrial plant"
       style="left:0;top:343px;width:339px;height:118px;background:linear-gradient(120deg,#6c7782,var(--photo-plant) 60%,#232a31)"></div>
  <div class="green-bar" style="top:469px;height:16px"></div>
  <div class="footer-links" style="top:473px;color:var(--white)"><span>www.voltaform.com</span><span>www.coreflow-thermal.co.uk</span></div>
</section>

<section class="page page--contact">
  <div class="abs" style="left:0;top:0;width:351px;height:34px;background:var(--orange)"></div>
  <div class="abs" style="left:339px;top:34px;width:12px;height:234px;background:var(--orange)"></div>
  <div class="photo" role="img" aria-label="Glowing blue gear mechanisms over a dark background"
       style="left:0;top:34px;width:339px;height:284px;background:radial-gradient(ellipse at 55% 45%,#3f7cc4,var(--photo-gears) 55%,#0a1426)"></div>
  <p class="abs" style="left:14px;top:324px;width:330px;font-size:11.6px;line-height:1.5;font-weight:800;font-style:italic;color:var(--orange)">FOR FURTHER INFORMATION ABOUT HOW WE CAN HELP YOU, PLEASE CONTACT:</p>
  <div class="brand abs" style="left:16px;top:384px;color:var(--ink)"><span class="dot"></span>VoltaForm</div>
  <div class="abs" style="left:177px;top:373px;width:1px;height:48px;background:var(--ink)"></div>
  <div class="brand abs" style="left:186px;top:385px;color:var(--ink);font-size:13.5px"><span class="dot"></span>CoreFlow Thermal</div>
  <div class="abs" style="left:14px;top:423px;font-size:6.6px;line-height:1.9;font-weight:600;white-space:nowrap">
    <p>✉ lena.hartmann@voltaform.com</p>
    <p>◎ www.voltaform.com</p>
  </div>
  <div class="abs" style="left:186px;top:423px;font-size:6.6px;line-height:1.9;font-weight:600;white-space:nowrap">
    <p>✉ mark.ellis@coreflow-thermal.co.uk</p>
    <p>◎ www.coreflow-thermal.co.uk</p>
  </div>
  <div class="green-bar" style="top:484px;height:8px"></div>
</section>

</body>
</html>
```